Business Card for Jewelry Business

We need a new namecard design for a jewelry company based in Bangkok, Thailand. We have a new website recently and want the new namecard to reflect our new modern image. I have uploaded our old namecard to show you the information that needs to be on the namecard. Pls check our website www.qelburn.com for the new color scheme to help design the new namecard.

```html
<!DOCTYPE html>
<html lang="en">
<head>
<meta charset="utf-8">
<title>Qelburn Jewellers – Business Card</title>
<link rel="stylesheet" href="https://fonts.googleapis.com/css2?family=Playfair+Display:wght@400&family=Questrial&display=swap">
<style>
  :root {
    --bg: #2a2c2f;
    --card-white: #ffffff;
    --card-black: #1e1e1f;
    --teal: #4bbfc5;
    --beige: #d9d2c7;
    --ink: #1a1a1a;
    --light: #f2f2f2;
  }
  * { margin: 0; padding: 0; box-sizing: border-box; }
  html, body { width: 1200px; height: 900px; overflow: hidden; }
  body {
    background: var(--bg);
    display: flex;
    align-items: center;
    justify-content: center;
    gap: 40px;
    font-family: "Questrial", "Century Gothic", sans-serif;
  }
  .card {
    position: relative;
    width: 540px;
    height: 310px;
    border-radius: 18px;
    overflow: hidden;
  }
  .card-front { background: var(--card-white); }
  .card-back {
    background: var(--card-black);
    display: flex;
    align-items: center;
    justify-content: center;
  }
  .card-shapes { position: absolute; inset: 0; }
  .holder-name {
    position: absolute; left: 30px; top: 26px;
    font-family: "Playfair Display", Georgia, serif;
    font-size: 24px; letter-spacing: 1px;
    color: var(--teal);
  }
  .holder-title {
    position: absolute; left: 30px; top: 60px;
    font-size: 12px; color: var(--ink);
  }
  .contact {
    position: absolute; left: 22px; top: 108px;
    color: var(--light); font-size: 11px; line-height: 17px;
  }
  .contact-row { display: flex; gap: 10px; white-space: nowrap; }
  .contact-item { display: inline-flex; align-items: center; gap: 4px; }
  .contact-item svg { width: 9px; height: 9px; fill: var(--teal); }
  .address { margin-top: 6px; }
  .wordmark {
    font-family: "Playfair Display", Georgia, serif;
    font-weight: 400;
    color: var(--ink);
    text-align: right;
  }
  .front-wordmark {
    position: absolute; right: 26px; top: 30px;
  }
  .wordmark-main { display: block; font-size: 38px; letter-spacing: 3px; line-height: 1; }
  .wordmark-sub { display: block; font-size: 13px; letter-spacing: 2.5px; margin-top: 6px; }
  .back-brand { display: flex; align-items: center; gap: 18px; }
  .back-brand .brand-dot {
    width: 46px; height: 46px; border-radius: 50%; background: var(--teal);
  }
  .back-brand .wordmark { color: var(--light); text-align: left; }
  .back-brand .wordmark-main { font-size: 42px; }
</style>
</head>
<body>
  <section class="card card-front">
    <svg class="card-shapes" viewBox="0 0 540 310" aria-hidden="true">
      <polygon points="0,96 420,96 350,268 0,268" fill="var(--card-black)"/>
      <polygon points="330,310 540,310 540,150 450,150" fill="var(--teal)"/>
      <circle cx="390" cy="212" r="84" fill="var(--card-white)"/>
      <circle cx="390" cy="212" r="76" fill="none" stroke="var(--beige)" stroke-width="2"/>
    </svg>

    <h1 class="holder-name">MALI TANAPORN</h1>
    <p class="holder-title">Sales &amp; Product Development Manager</p>

    <div class="wordmark front-wordmark">
      <span class="wordmark-main">QELBURN</span>
      <span class="wordmark-sub">JEWELLERS</span>
    </div>

    <div class="contact">
      <div class="contact-row">
        <span class="contact-item"><svg viewBox="0 0 10 10"><path d="M2 0h2l1 3-1.5 1a6 6 0 0 0 2.5 2.5L7 5l3 1v2a2 2 0 0 1-2 2A8 8 0 0 1 0 2a2 2 0 0 1 2-2z"/></svg>+662-410-5523-6</span>
        <span class="contact-item"><svg viewBox="0 0 10 10"><path d="M2 0h2l1 3-1.5 1a6 6 0 0 0 2.5 2.5L7 5l3 1v2a2 2 0 0 1-2 2A8 8 0 0 1 0 2a2 2 0 0 1 2-2z"/></svg>+662-581-2290</span>
        <span class="contact-item"><svg viewBox="0 0 10 10"><path d="M0 2h10v6H0z M0 2l5 3 5-3" stroke="var(--card-black)" stroke-width=".8"/></svg>mali@qelburn.com</span>
      </div>
      <div class="contact-row">
        <span class="contact-item"><svg viewBox="0 0 10 10"><path d="M0 2h10v6H0z M0 2l5 3 5-3" stroke="var(--card-black)" stroke-width=".8"/></svg>hello@qelburn.com</span>
        <span class="contact-item"><svg viewBox="0 0 10 10"><circle cx="5" cy="5" r="5"/></svg>www.qelburn.com</span>
      </div>
      <div class="contact-row">
        <span class="contact-item"><svg viewBox="0 0 10 10"><circle cx="5" cy="5" r="5"/></svg>Qelburn Jewellers</span>
        <span class="contact-item"><svg viewBox="0 0 10 10"><rect width="10" height="10" rx="2"/></svg>QelburnJwl</span>
      </div>
      <p class="address">Qelburn Jewellers Co., Ltd.<br>
      218 Moo 7 Rattanakosin Road, Trade Zone 2,<br>
      Bang Phli Industrial Park, Bang Phli,<br>
      Bangkok 10540 Thailand</p>
    </div>
  </section>

  <section class="card card-back">
    <div class="back-brand">
      <span class="brand-dot"></span>
      <div class="wordmark">
        <span class="wordmark-main">QELBURN</span>
        <span class="wordmark-sub">JEWELLERS</span>
      </div>
    </div>
  </section>
</body>
</html>
```